Wren Vehicle Polishing (Mobile detail)

I need a business card made up. I'd like it to be different in some form, either raised, embossed, debossed, something cool that stands out. (preferably embossed text somewhere in it). I will be including the Initial png file. Let me know if you need the photoshop of adobe illustrator file to work with.
Updates

Information to be included: Text: XXX-XXX-XXXX Phone: XXX-XXX-XXXX Email: wrenvehiclepolish@mailnest.example Website: www.socialpage.example/wrenvehiclepolishKTR Hours of operation: Mon - Fri 7:00AM to 8:00PM Sat - 10:00AM to 8:00PM

Target Market(s)

Mobile automotive detailing

Industry/Entity Type

Automotive

Contact Information for Business Card

Make it stand out with embossed lettering, I'd also like the background to be glossy black or matte, something that represents a shiny car, black preferred

Requirements
Must have
• A glossy background, or something.
• My logo, pick one of them that best fits your design.
Should not have
• White background,
• something that does not stand out.

```html
<!DOCTYPE html>
<html lang="en">
<head>
<meta charset="utf-8">
<title>Wren Vehicle Polishing – Business Card</title>
<link href="https://fonts.googleapis.com/css2?family=Open+Sans:wght@400;600;700&display=swap" rel="stylesheet">
<style>
  :root {
    --accent: #f05a22;
    --ink: #f2f2f2;
    --ink-soft: #c9c9c9;
    --card-top: #3a3a3c;
    --card-mid: #121213;
    --card-bottom: #050505;
    --backdrop: #d9d9d9;
  }
  * { margin: 0; padding: 0; box-sizing: border-box; }
  html, body { width: 1200px; height: 900px; overflow: hidden; }
  body {
    background: var(--backdrop);
    font-family: "Open Sans", Arial, sans-serif;
    color: var(--ink);
    position: relative;
  }
  .card {
    position: absolute;
    left: 80px; top: 130px;
    width: 1040px; height: 640px;
    border-radius: 32px;
    background:
      linear-gradient(160deg, rgba(255,255,255,0.16) 0%, rgba(255,255,255,0.04) 38%, rgba(255,255,255,0) 39%),
      linear-gradient(180deg, var(--card-top) 0%, var(--card-mid) 45%, var(--card-bottom) 100%);
    box-shadow: 0 18px 40px rgba(0,0,0,0.35), inset 0 1px 0 rgba(255,255,255,0.25);
    overflow: hidden;
  }
  .embossed {
    text-shadow: -1px -1px 0 rgba(255,255,255,0.35), 1px 2px 2px rgba(0,0,0,0.9);
  }
  .brand {
    position: absolute;
    left: 70px; top: 150px;
    width: 380px;
    display: flex; align-items: center; gap: 18px;
  }
  .brand-dot {
    flex: 0 0 56px; height: 56px;
    border-radius: 50%;
    background: var(--accent);
  }
  .brand-name {
    font-size: 40px; font-weight: 700; line-height: 1.1;
    color: var(--ink);
  }
  .person { position: absolute; left: 504px; top: 82px; }
  .person-name { font-size: 38px; font-weight: 600; color: var(--accent); line-height: 1.2; }
  .person-role { font-size: 26px; font-weight: 400; color: var(--ink-soft); line-height: 1.3; }
  .contacts {
    position: absolute; left: 506px; top: 244px;
    list-style: none;
  }
  .contacts li {
    display: flex; align-items: center; gap: 12px;
    height: 44px;
    font-size: 21px; letter-spacing: -0.2px;
    color: var(--ink);
  }
  .contacts svg { width: 18px; height: 18px; fill: var(--accent); flex: 0 0 18px; }
  .hours-title {
    position: absolute; left: 0; right: 0; top: 510px;
    display: flex; align-items: center; gap: 24px;
    font-size: 35px; font-weight: 600; color: var(--accent);
    white-space: nowrap;
  }
  .hours-title::before, .hours-title::after {
    content: ""; flex: 1; height: 2px; background: var(--accent);
  }
  .hours {
    position: absolute; left: 0; right: 0; top: 566px;
    text-align: center;
    font-size: 29px; font-weight: 600; color: var(--ink);
  }
  .hours .day { color: var(--accent); }
</style>
</head>
<body>
  <section class="card">
    <div class="brand">
      <span class="brand-dot"></span>
      <span class="brand-name">Wren Vehicle Polishing</span>
    </div>

    <div class="person">
      <p class="person-name embossed">Marlow Ashby</p>
      <p class="person-role embossed">Managing Director</p>
    </div>

    <ul class="contacts">
      <li><svg viewBox="0 0 24 24"><path d="M6.6 10.8a15.1 15.1 0 0 0 6.6 6.6l2.2-2.2a1 1 0 0 1 1-.25 11.4 11.4 0 0 0 3.6.57 1 1 0 0 1 1 1V20a1 1 0 0 1-1 1A17 17 0 0 1 3 4a1 1 0 0 1 1-1h3.5a1 1 0 0 1 1 1c0 1.25.2 2.45.57 3.57a1 1 0 0 1-.25 1z"/></svg>XXX-XXX-XXXX</li>
      <li><svg viewBox="0 0 24 24"><path d="M7 1h10a2 2 0 0 1 2 2v18a2 2 0 0 1-2 2H7a2 2 0 0 1-2-2V3a2 2 0 0 1 2-2zm0 3v14h10V4zm5 15.5a1 1 0 1 0 0 2 1 1 0 0 0 0-2z"/></svg>XXX-XXX-XXXX</li>
      <li><svg viewBox="0 0 24 24"><path d="M2 5h20v14H2zm2 2v.5l8 5 8-5V7l-8 5z"/></svg>wrenvehiclepolish@mailnest.example</li>
      <li><svg viewBox="0 0 24 24"><path d="M12 2a10 10 0 1 0 0 20 10 10 0 0 0 0-20zm-1 17.9A8 8 0 0 1 4.2 10.8L9 15.6v1a2 2 0 0 0 2 2zm6.9-2.5A2 2 0 0 0 16 16h-1v-3a1 1 0 0 0-1-1H8v-2h2a1 1 0 0 0 1-1V7h2a2 2 0 0 0 2-2v-.4a8 8 0 0 1 2.9 12.8z"/></svg>www.socialpage.example/wrenvehiclepolishKTR</li>
    </ul>

    <h2 class="hours-title embossed">KTR Hours of operation</h2>
    <p class="hours embossed"><span class="day">Mon - Fri:</span> 7:00AM to 8:00PM <span class="day">&nbsp;|&nbsp;Sat:</span> 10:00AM to 8:00PM</p>
  </section>
</body>
</html>
```